Wordpress Theme for a Professional Speaker's Website

I I need a website to promote myself as a speaker to corporations and meeting planners. Some examples of similar sites I like are:

http://www.beginwithpurpose.example (this is by far my favorite)
http://www.tovaruskin.example
http://www.glenbeckworth.example
http://www.lomtrisel.example
http://www.dawnafterstorms.example
http://www.osricpellandine.example

I like modern, minimalistic, innovative. I'm okay if it's edgy but still want it communicate professionalism.

The primary objective is to position me as an expert who can deliver valuable information in an entertaining manner.

There are two calls to action. The first is to capture name and email address to subscribe to my newsletter. The second is to request more information about booking me to speak for their company, organization, etc.

The pages on the website will ultimately be the following:

1. Home (should include sections for recent blog posts, featured topics/presentations, short bio, testimonials, email capture, and anything else you think should be added.
2. Meet Ross
3. Blog
4. Keynotes & Speaking
5. Training & Webinars
6. Coaching & Consulting
7. Testimonials
8. Book Ross
9. Media Inquiries
10. Contact

Please feel free to use your creativity. I don't want my requirements to limit you in any way. I'm just looking for a modern, professional site that will make me stand out from the crowd.

I don't have any existing site or brand identity. My plan is to have the website design I ultimately choose serve as the foundation for the rest of my brand identity.

Target Market(s)

Corporate meeting planners and executives

Industry/Entity Type

It Professional

Font styles to use
Sans Serif

Requirements
Must have
• Email capture, testimonials, blog
Nice to have
• None
Should not have
• None

```html
<!DOCTYPE html>
<html lang="en">
<head>
<meta charset="utf-8">
<title>Meet Ross – Speaker Home</title>
<link href="https://fonts.googleapis.com/css2?family=Open+Sans:ital,wght@0,400;0,600;0,700;1,400&family=Lato:wght@400;700;900&family=Ubuntu:wght@500;700&display=swap" rel="stylesheet">
<style>
:root{
  --stage:#2b2b2d;
  --navy:#2a1f55;
  --hero:#3d3660;
  --gold:#d4a42a;
  --amber:#ebb219;
  --sky:#3f9ad9;
  --orange:#e8642b;
  --lime:#8fe01a;
  --white:#ffffff;
  --ink:#333333;
  --muted:#9a9a9a;
  --link:#3a8fd6;
}
*{box-sizing:border-box;margin:0;padding:0}
html,body{width:960px;height:1200px;overflow:hidden;background:var(--stage);font-family:'Open Sans',sans-serif}
.page{position:absolute;left:271px;top:0;width:494px;height:1418px;background:var(--white);transform:scale(.8463);transform-origin:0 0;overflow:hidden}
.band{position:absolute;left:0;width:494px}
.abs{position:absolute}
.center{text-align:center}

/* header */
.site-header{top:21px;height:60px;background:var(--navy)}
.brand{top:12px;width:100%;font-size:13px;color:var(--white);letter-spacing:.5px;font-weight:400}
.main-nav{top:37px;left:21px;right:21px;display:flex;justify-content:space-between;font-size:5.6px;font-weight:700;color:var(--white);list-style:none}
.main-nav .active{color:#f5b21c}

/* hero */
.hero{top:81px;height:235px;background:var(--hero)}
.hero-title{left:52px;top:50px;font-size:20px;font-weight:700;color:var(--white);letter-spacing:.3px}
.hero-bio{left:40px;top:92px;width:220px;font-size:6.6px;line-height:8.8px;font-style:italic;color:var(--white)}
.hero-photo{left:282px;top:0;width:184px;height:235px;background:linear-gradient(160deg,#9aa9a4 0%,#5a6a6e 45%,#1f2a3c 100%)}

/* newsletter */
.newsletter{top:316px;height:89px;background:var(--gold)}
.newsletter h2{top:15px;width:100%;font-size:11.5px;font-weight:700;color:var(--white);letter-spacing:.2px}
.field{top:46px;height:18px;border:1px solid #f3e1a8;font-size:6.5px;color:#fff6d8;padding:4px 4px;background:transparent}
.join{left:333px;top:46px;width:134px;height:18px;background:var(--navy);color:var(--white);font-size:11px;font-weight:700;text-align:center;line-height:18px}

/* services */
.services{top:405px;height:174px;background:var(--navy)}
.services h2{top:11px;width:100%;font-size:11.5px;font-weight:700;color:var(--white)}
.service-photo{top:36px;width:98px;height:98px;border-radius:50%}
.service-label{top:148px;width:130px;font-size:7px;font-weight:700;color:var(--white);text-align:center}

/* blog */
.blog{top:579px;height:222px;background:var(--white)}
.blog h2{top:9px;width:100%;font-size:11.5px;font-weight:600;color:#555}
.post-image{top:34px;width:142px;height:95px}
.post-date{top:137px;width:22px;height:20px;background:var(--orange);color:var(--white);font-size:5.5px;font-weight:700;text-align:center;line-height:7px;padding-top:3px}
.post-title{top:137px;font-size:7.5px;font-weight:600;color:#555;white-space:nowrap;width:114px;overflow:hidden}
.post-meta{top:149px;font-size:4.6px;color:var(--muted);font-weight:600}
.post-excerpt{top:164px;width:140px;font-size:5.8px;line-height:8px;color:#aaa}
.post-more{top:200px;width:142px;text-align:right;font-size:5.8px;color:var(--link)}

/* featured */
.featured{top:801px;height:168px;background:var(--navy)}
.featured h2{top:13px;width:100%;font-size:11.5px;font-weight:700;color:var(--white)}
.topic{top:45px;width:145px;height:103px}
.topic-bar{position:absolute;left:0;right:0;bottom:0;height:29px;background:rgba(200,190,230,.78);padding:5px 0 0 11px;font-size:7px;line-height:9px;font-weight:600;color:#3d3660}
.topic-go{position:absolute;right:8px;bottom:5px;width:19px;height:19px;background:#e0a71d}

/* call to action */
.booking{top:969px;height:137px;background:var(--amber)}
.booking h2{left:40px;top:20px;width:254px;font-family:'Ubuntu',sans-serif;font-size:14px;line-height:18px;font-weight:700;color:var(--white);text-align:center}
.booking-btn{left:97px;top:85px;width:120px;height:22px;background:var(--orange);border:1px solid var(--white);color:var(--white);font-size:6.5px;font-weight:700;text-align:center;line-height:20px}
.booking-photo{left:307px;top:17px;width:99px;height:105px;background:linear-gradient(135deg,#c53a1f 0%,#3a1a14 40%,#0b0b10 100%)}

/* testimonials */
.testimonials{top:1106px;height:242px;background:var(--sky);font-family:'Lato',sans-serif}
.testimonials h2{top:32px;width:100%;font-size:17px;font-weight:900;color:var(--white)}
.testimonials .lede{top:62px;width:100%;font-size:8px;font-weight:700;color:var(--white)}
.quote{top:140px;width:142px;height:96px;border:1px solid #cfe6f7;color:var(--white);text-align:center;padding:24px 8px 0}
.quote p{font-size:5.8px;line-height:8.6px}
.quote .who{margin-top:12px;font-size:6.5px;font-weight:900}
.quote .org{font-size:4.6px}
.avatar{top:121px;width:36px;height:36px;border-radius:50%;border:2px solid var(--white)}

/* footer */
.site-footer{top:1348px;height:32px;background:var(--amber)}
.site-footer p{top:12px;width:100%;font-size:5.2px;font-weight:700;color:#333}
</style>
</head>
<body>
<div class="page">

  <header class="band site-header">
    <div class="abs brand center">MEET ROSS</div>
    <ul class="abs main-nav">
      <li class="active">HOME</li><li>MEET ROSS</li><li>BLOG</li><li>KEYNOTES &amp; SPEAKERS</li><li>TRAINING</li><li>COACHING</li><li>TESTIMONIALS</li><li>BOOK ROSS</li><li>MEDIA ENQUIRIES</li><li>CONTACT</li>
    </ul>
  </header>

  <section class="band hero">
    <h1 class="abs hero-title">TITLE (SHORT BIO)</h1>
    <p class="abs hero-bio center">Lorem Ipsum is simply dummy text of the printing and typesetting industry. Lorem Ipsum has been the industry's standard dummy text ever since the 1500s, when an unknown printer took a galley of type and scrambled it to make a type specimen book. It has survived not only five centuries, but also the leap into electronic typesetting, remaining essentially unchanged. It was popularised in the 1960s with the release of Letraset sheets containing Lorem Ipsum passages, and more recently with desktop publishing software like Aldus PageMaker including versions of Lorem Ipsum.</p>
    <div class="abs hero-photo" role="img" aria-label="Portrait of Ross in a dark suit, arms crossed, by a bright window"></div>
  </section>

  <section class="band newsletter">
    <h2 class="abs center">JOIN MY NEWSLETTER FOR MORE REGULAR UPDATES</h2>
    <div class="abs field" style="left:23px;width:148px">First Name</div>
    <div class="abs field" style="left:179px;width:148px">Enter Email Address</div>
    <div class="abs join">JOIN NOW</div>
  </section>

  <section class="band services">
    <h2 class="abs center">HOW CAN WE HELP YOU ?</h2>
    <div class="abs service-photo" style="left:19px;background:radial-gradient(circle at 50% 45%,#f2f2f2 0%,#c9c4bb 60%,#8d7c62 100%)" role="img" aria-label="Headshot of Ross"></div>
    <div class="abs service-photo" style="left:136px;background:radial-gradient(circle at 50% 55%,#d89a90 0%,#5a2a22 45%,#120a0a 100%)" role="img" aria-label="Ross giving a keynote on stage"></div>
    <div class="abs service-photo" style="left:255px;background:radial-gradient(circle at 50% 60%,#e0a39a 0%,#4a2220 45%,#0d0808 100%)" role="img" aria-label="Ross presenting a training session"></div>
    <div class="abs service-photo" style="left:373px;background:radial-gradient(circle at 50% 55%,#a89a92 0%,#3a2f2d 45%,#0a0a0c 100%)" role="img" aria-label="Ross coaching from the stage"></div>
    <div class="abs service-label" style="left:3px">First Time ( Click Here)</div>
    <div class="abs service-label" style="left:120px">Keynotes &amp; Speaking</div>
    <div class="abs service-label" style="left:239px">Training &amp; Webinars</div>
    <div class="abs service-label" style="left:357px">Coaching &amp; Consultancy</div>
  </section>

  <section class="band blog">
    <h2 class="abs center">Recent Blog Posts</h2>

    <div class="abs post-image" style="left:22px;background:linear-gradient(135deg,#8a6a4a,#3a2a1e)" role="img" aria-label="Craftsman at a cluttered workbench"></div>
    <div class="abs post-date" style="left:22px">11<br>Apr</div>
    <div class="abs post-title" style="left:50px">My New Post ! Please stay</div>
    <div class="abs post-meta" style="left:50px">Posted by admin in World</div>
    <p class="abs post-excerpt" style="left:22px">Lorem ipsum dolor sit amet, consectetur adipisicing elit. Sint, odio eum magni optio laborum non et accusamus, itaque.Lorem ipsum dolor sit amet, cons</p>
    <div class="abs post-more" style="left:22px">Continue Reading..</div>

    <div class="abs post-image" style="left:176px;background:linear-gradient(180deg,#3a3a3c,#6a6c70 60%,#2e2e30)" role="img" aria-label="Open-plan office interior"></div>
    <div class="abs post-date" style="left:176px">25<br>Mar</div>
    <div class="abs post-title" style="left:204px">The Journey to Product Ma</div>
    <div class="abs post-meta" style="left:204px">Posted by admin in World</div>
    <p class="abs post-excerpt" style="left:176px">Lorem ipsum dolor sit amet, consectetur adipisicing elit. Sint, odio eum magni optio laborum non et accusamus, itaque.Lorem ipsum dolor sit amet, cons</p>
    <div class="abs post-more" style="left:176px">Continue Reading..</div>

    <div class="abs post-image" style="left:330px;background:linear-gradient(180deg,#e6e3e8,#cfcbd2)" role="img" aria-label="Minimal desk with monitor and plant"></div>
    <div class="abs post-date" style="left:330px">25<br>Mar</div>
    <div class="abs post-title" style="left:358px">Your Start to Finish Guid</div>
    <div class="abs post-meta" style="left:358px">Posted by admin in World</div>
    <p class="abs post-excerpt" style="left:330px">Lorem ipsum dolor sit amet, consectetur adipisicing elit. Sint, odio eum magni optio laborum non et accusamus, itaque. Lorem ipsum dolor sit amet, co</p>
    <div class="abs post-more" style="left:330px">Continue Reading..</div>
  </section>

  <section class="band featured">
    <h2 class="abs center">FEATURED TOPICS</h2>
    <div class="abs topic" style="left:17px;background:linear-gradient(135deg,#4a4e58,#1e2028)" role="img" aria-label="Young man in glasses thinking">
      <div class="topic-bar">My New Featured Post<br>Title - 01</div>
      <svg class="topic-go" viewBox="0 0 19 19"><rect width="19" height="19" fill="#e0a71d"/><path d="M8 6l4 3.5L8 13" stroke="#fff" stroke-width="1.6" fill="none"/></svg>
    </div>
    <div class="abs topic" style="left:173px;background:linear-gradient(135deg,#2e3a5e,#c8ccd6)" role="img" aria-label="Hand writing with a pen">
      <div class="topic-bar">My New Featured Post<br>Title - 02</div>
      <svg class="topic-go" viewBox="0 0 19 19"><rect width="19" height="19" fill="#e0a71d"/><path d="M8 6l4 3.5L8 13" stroke="#fff" stroke-width="1.6" fill="none"/></svg>
    </div>
    <div class="abs topic" style="left:330px;background:linear-gradient(135deg,#d8dde4,#3a4c6a)" role="img" aria-label="Two people working at computers">
      <div class="topic-bar">My New Featured Post<br>Title-03</div>
      <svg class="topic-go" viewBox="0 0 19 19"><rect width="19" height="19" fill="#e0a71d"/><path d="M8 6l4 3.5L8 13" stroke="#fff" stroke-width="1.6" fill="none"/></svg>
    </div>
  </section>

  <section class="band booking">
    <h2 class="abs">Want me to speak for your company, organization&nbsp; ?</h2>
    <div class="abs booking-btn">Reserve A Consultation Now !</div>
    <div class="abs booking-photo" role="img" aria-label="Ross speaking into a microphone on stage"></div>
  </section>

  <section class="band testimonials">
    <h2 class="abs center">What People Are Saying About Us</h2>
    <p class="abs lede center">Meet our happy clients and find why our Agency is the preferred choice.</p>

    <div class="abs quote" style="left:22px"><p>Illum timeam maiestatis his te. Ei mel eirmod legendos, quis moderatius ea mea, vix viris dignissim contentiones no. Sint facilisis ad eam. Vix an illud assentiet.</p><div class="who">Carol Miller</div><div class="org">Awesome Lorem Studio</div></div>
    <div class="abs quote" style="left:176px"><p>Illum timeam maiestatis his te. Ei mel eirmod legendos, quis moderatius ea mea, vix viris dignissim contentiones no. Sint facilisis ad eam. Vix an illud assentiet.</p><div class="who">Brandon Riley</div><div class="org">Smart Lorem Agency</div></div>
    <div class="abs quote" style="left:330px"><p>Illum timeam maiestatis his te. Ei mel eirmod legendos, quis moderatius ea mea, vix viris dignissim contentiones no. Sint facilisis ad eam. Vix an illud assentiet.</p><div class="who">Jonathan Lawson</div><div class="org">Intrepid Ipsum Enterpreneurs</div></div>

    <div class="abs avatar" style="left:31px;background:linear-gradient(135deg,#c9a98a,#5a3a2a)" role="img" aria-label="Client photo, Carol Miller"></div>
    <div class="abs avatar" style="left:185px;background:linear-gradient(135deg,#d8c4b0,#6a8aa8)" role="img" aria-label="Client photo, Brandon Riley"></div>
    <div class="abs avatar" style="left:339px;background:linear-gradient(135deg,#b08a6a,#3a2a22)" role="img" aria-label="Client photo, Jonathan Lawson"></div>
  </section>

  <footer class="band site-footer">
    <p class="abs center">COPYRIGHT © 2016 MEETROSS</p>
  </footer>

</div>
</body>
</html>
```